Window Signage to Attract Customers

We need someone to design several window signs for our retail business. These sign graphics will be printed on window cling or vinyl window decal material and ultimately attached to our store windows. The style of the signs should be consistent (please see word document for sign copy). The rough size of these window signs will be approximately 4ft x 3ft and may be reduced to 3ft x 2ft (poster size) so graphics should allow for that. I have attached an example of a competitor's signs. I have also attached our logo and other signs we have to use as examples of our colors and for style inspiration.
Target Market(s)
Drive and walk by consumers

```html
<!DOCTYPE html>
<html lang="en">
<head>
<meta charset="UTF-8">
<title>Title Loans Window Sign</title>
<link rel="stylesheet" href="https://fonts.googleapis.com/css2?family=Luckiest+Guy&family=Open+Sans:wght@400;800&display=swap">
<style>
  :root {
    --backdrop: #e9e6e1;
    --sign-yellow: #f5a90f;
    --sign-yellow-light: #fbbf2e;
    --sign-blue: #1557b8;
    --sign-blue-dark: #0d3f8c;
    --frame-shadow: #0b1d3a;
    --ink-black: #111111;
    --paper-white: #ffffff;
  }
  html, body {
    margin: 0;
    padding: 0;
    width: 1200px;
    height: 800px;
    overflow: hidden;
    background: var(--backdrop);
  }
  .window-sign {
    display: block;
    width: 1200px;
    height: 800px;
  }
  .headline {
    font-family: "Luckiest Guy", "Arial Black", sans-serif;
    text-anchor: middle;
  }
  .headline-outer {
    fill: var(--sign-blue);
    stroke: var(--sign-blue);
    stroke-width: 16px;
    stroke-linejoin: round;
  }
  .headline-inner {
    fill: var(--ink-black);
    stroke: var(--paper-white);
    stroke-width: 6px;
    stroke-linejoin: round;
    paint-order: stroke;
  }
  .amount-shadow {
    fill: var(--sign-blue-dark);
    stroke: var(--sign-blue-dark);
    stroke-width: 8px;
    stroke-linejoin: round;
  }
  .amount {
    fill: var(--sign-blue);
    stroke: var(--paper-white);
    stroke-width: 5px;
    stroke-linejoin: round;
    paint-order: stroke;
  }
  .fine-print {
    font-family: "Open Sans", Arial, sans-serif;
    font-size: 11.5px;
    fill: var(--paper-white);
    text-anchor: middle;
  }
  .brand-name {
    font-family: "Open Sans", Arial, sans-serif;
    font-weight: 800;
    font-size: 30px;
    fill: var(--sign-blue);
  }
</style>
</head>
<body>
<svg class="window-sign" viewBox="0 0 1200 800" xmlns="http://www.w3.org/2000/svg">
  <defs>
    <radialGradient id="burst" cx="0.5" cy="0.5" r="0.6">
      <stop offset="0" stop-color="var(--sign-yellow-light)"/>
      <stop offset="1" stop-color="var(--sign-yellow)"/>
    </radialGradient>
  </defs>

  <!-- Blue square frame -->
  <g class="frame">
    <polygon points="448,156 884,308 788,660 364,512" fill="none" stroke="var(--frame-shadow)" stroke-width="20" transform="translate(6,6)"/>
    <polygon points="448,156 884,308 788,660 364,512" fill="none" stroke="var(--sign-blue)" stroke-width="20"/>
  </g>

  <!-- Yellow brush strokes -->
  <g class="brush-strokes" fill="url(#burst)">
    <polygon points="330,276 700,174 708,200 462,268 800,226 818,250 420,326 360,320"/>
    <polygon points="380,300 820,220 826,252 850,244 860,300 430,380 380,372"/>
    <polygon points="360,360 900,236 920,272 940,400 420,500 372,470"/>
    <polygon points="360,420 960,338 950,376 870,470 500,560 370,520"/>
    <polygon points="400,480 900,420 880,520 620,600 420,560"/>
    <polygon points="560,560 930,440 900,500 760,630 600,636"/>
    <polygon points="620,600 880,520 840,590 700,640"/>
  </g>

  <!-- Headline -->
  <g class="headline-title" transform="rotate(-15 594 260)">
    <text class="headline headline-outer" x="594" y="290" font-size="84" textLength="200" lengthAdjust="spacingAndGlyphs">TITLE</text>
    <text class="headline headline-inner" x="594" y="290" font-size="84" textLength="200" lengthAdjust="spacingAndGlyphs">TITLE</text>
  </g>
  <g class="headline-loans" transform="rotate(-15 590 356)">
    <text class="headline headline-outer" x="590" y="392" font-size="98" textLength="280" lengthAdjust="spacingAndGlyphs">LOANS</text>
    <text class="headline headline-inner" x="590" y="392" font-size="98" textLength="280" lengthAdjust="spacingAndGlyphs">LOANS</text>
  </g>

  <!-- Amounts -->
  <g class="amount-low" transform="rotate(-15 642 440)">
    <text class="headline amount-shadow" x="642" y="462" font-size="58" textLength="190" lengthAdjust="spacingAndGlyphs" transform="translate(4,5)">$2,510</text>
    <text class="headline amount" x="642" y="462" font-size="58" textLength="190" lengthAdjust="spacingAndGlyphs">$2,510</text>
  </g>
  <g class="amount-high" transform="rotate(-15 690 500)">
    <text class="headline amount-shadow" x="690" y="524" font-size="62" textLength="240" lengthAdjust="spacingAndGlyphs" transform="translate(4,5)">$25,000</text>
    <text class="headline amount" x="690" y="524" font-size="62" textLength="240" lengthAdjust="spacingAndGlyphs">$25,000</text>
  </g>
  <text class="headline amount" x="802" y="452" font-size="36">*</text>

  <!-- Disclaimer circle -->
  <g class="disclaimer">
    <circle cx="376" cy="572" r="126" fill="var(--sign-yellow)"/>
    <circle cx="384" cy="568" r="124" fill="var(--sign-blue)"/>
    <text class="fine-print" x="384" y="516">*Approval depends on</text>
    <text class="fine-print" x="384" y="531">meeting legal and underwriting</text>
    <text class="fine-print" x="384" y="546">requirements.  All product and service</text>
    <text class="fine-print" x="384" y="561">options are subject to change without</text>
    <text class="fine-print" x="384" y="576">notice.  See store for details.</text>
    <text class="fine-print" x="384" y="591">Auto Title Loans &amp; Personal Loans are</text>
    <text class="fine-print" x="384" y="606">arranged and made pursuant to a</text>
    <text class="fine-print" x="384" y="621">State Consumer Lending Board</text>
    <text class="fine-print" x="384" y="636">Financing Law License.</text>
  </g>

  <!-- Brand -->
  <g class="brand">
    <rect x="506" y="672" width="20" height="20" fill="var(--sign-yellow)"/>
    <text class="brand-name" x="536" y="693">Tallowbrook Loans</text>
  </g>
</svg>
</body>
</html>
```